Flyer Mail out

Need something urgently designed.

I need a flyer done double sided I have provided CWDG photos and the writing. I do not have any dental surgery stock photos as such but this can be used. We are a mobile dental company that goes out to schools and provide free dental services.

I have attached the written document and would like it double sided A4 paper.

The colours I want is Aqua, Light Blue, dark blue, grey and white.

Just need it designed beautifully and professionally to go out to principals to contact us and use our services.

If you would like more info have a look at our Chatterloop page Coastline Wandering Dental Group

```html
<!DOCTYPE html>
<html lang="en">
<head>
<meta charset="utf-8">
<title>CWDG School Flyer</title>
<link href="https://fonts.googleapis.com/css2?family=Roboto+Condensed:wght@300;400;700&family=Open+Sans:wght@400;600;700&display=swap" rel="stylesheet">
<style>
  :root{
    --aqua:#4fc3d3;
    --aqua-deep:#2fa7ba;
    --light-blue:#bfe6ec;
    --pale:#e4f4f6;
    --navy:#1c5f70;
    --grey:#7d8589;
    --grey-dark:#5b6266;
    --white:#ffffff;
    --stage:#d9dcde;
  }
  *{box-sizing:border-box;margin:0;padding:0}
  html,body{width:1200px;height:894px;overflow:hidden}
  body{background:var(--stage);font-family:"Open Sans",Arial,sans-serif;position:relative}

  .page{position:absolute;top:187px;width:368px;height:520px;background:var(--white);overflow:hidden;box-shadow:0 4px 14px rgba(0,0,0,.18)}
  .inside-left{left:28px}
  .inside-right{left:396px}
  .cover{left:804px}

  /* inside left */
  .team-photo{position:absolute;left:0;top:0;width:100%;height:340px;
    background:linear-gradient(160deg,#a9dbe3 0%,#6fbfcc 45%,#3e9fb1 100%)}
  .book-call{position:absolute;left:26px;top:370px;right:26px}
  .book-call .lead{font-family:"Roboto Condensed",Arial,sans-serif;font-weight:400;font-size:15px;line-height:1.2;color:var(--grey);text-transform:uppercase}
  .book-call .big{font-family:"Roboto Condensed",Arial,sans-serif;font-weight:700;font-size:46px;line-height:1;color:var(--grey);text-transform:uppercase;margin-top:6px}

  /* inside right */
  .letter{position:absolute;left:0;top:0;width:100%;height:140px;padding:20px 24px 0;background:var(--white)}
  .letter h2{font-family:"Roboto Condensed",Arial,sans-serif;font-weight:700;font-size:26px;color:var(--aqua-deep);margin-bottom:6px}
  .letter p{font-size:7px;line-height:1.45;color:var(--aqua-deep);margin-bottom:4px}
  .offers{position:absolute;left:0;top:140px;width:100%;height:220px;background:linear-gradient(180deg,var(--light-blue),var(--aqua));padding:14px 22px}
  .offers h3{font-family:"Roboto Condensed",Arial,sans-serif;font-weight:700;font-size:22px;color:var(--white);margin-bottom:10px}
  .offer-grid{display:grid;grid-template-columns:1fr 1fr;gap:12px 16px}
  .offer{text-align:center;color:var(--white)}
  .offer svg{width:20px;height:20px;display:block;margin:0 auto 3px}
  .offer h4{font-family:"Roboto Condensed",Arial,sans-serif;font-weight:700;font-size:8.5px;text-transform:uppercase;line-height:1.15;margin-bottom:3px}
  .offer p{font-size:6.5px;line-height:1.4}
  .about{position:absolute;left:0;top:360px;width:100%;height:160px;background:var(--aqua-deep);padding:16px 24px;color:var(--white)}
  .about p{font-size:7px;line-height:1.5;margin-bottom:6px}
  .about strong{font-weight:700}

  /* cover */
  .cover-top{position:absolute;left:0;top:0;width:100%;height:8px;background:var(--aqua)}
  .brand{position:absolute;left:0;top:8px;width:100%;height:58px;display:flex;align-items:center;justify-content:center}
  .brand .name{font-family:"Open Sans",Arial,sans-serif;font-weight:600;font-size:10px;color:var(--grey-dark)}
  .staff-photo{position:absolute;left:0;top:66px;width:100%;height:250px;
    background:linear-gradient(150deg,#9fd6df 0%,#6cc0cd 50%,#43a7b8 100%);
    clip-path:polygon(0 0,100% 0,100% 92%,26% 92%,19% 100%,12% 92%,0 92%)}
  .focus{position:absolute;left:34px;top:178px;color:var(--white);font-family:"Roboto Condensed",Arial,sans-serif;text-transform:uppercase}
  .focus .pre{font-weight:300;font-size:17px;letter-spacing:.5px}
  .focus .main{font-weight:700;font-size:42px;line-height:.98}
  .quote{position:absolute;left:30px;right:24px;top:340px;font-family:"Roboto Condensed",Arial,sans-serif;text-transform:uppercase}
  .quote blockquote{font-weight:300;font-size:11px;line-height:1.3;color:var(--aqua-deep)}
  .quote cite{display:block;font-style:normal;font-weight:700;font-size:11px;color:var(--aqua-deep);margin-top:2px}
  .quote .note{font-family:"Open Sans",Arial,sans-serif;font-size:5.5px;line-height:1.5;color:var(--grey);margin-top:12px}
  .cover-foot{position:absolute;left:0;bottom:0;width:100%;height:30px;background:linear-gradient(180deg,var(--aqua),var(--aqua-deep))}
</style>
</head>
<body>

<section class="page inside-left">
  <div class="team-photo" role="img" aria-label="Photo of the mobile dental team standing beside their van, tinted aqua"></div>
  <div class="book-call">
    <p class="lead">Book us now for 2015 and<br>help us bring back your student's</p>
    <p class="big">Bright Smile!</p>
  </div>
</section>

<section class="page inside-right">
  <div class="letter">
    <h2>Dear Principal,</h2>
    <p>We thank you for the time taken to read about Coastline Wandering Dental Group (CWDG). We are committed to the oral health of every student in your school.</p>
    <p>We are proudly operated by qualified dental professionals who travel to schools across the region and have treated more than 150 schools to date.</p>
    <p>We are pleased to introduce our service to your school and look forward to bringing better smiles to your students and families.</p>
  </div>
  <div class="offers">
    <h3>We offer:</h3>
    <div class="offer-grid">
      <div class="offer">
        <svg viewBox="0 0 24 24"><path fill="#fff" d="M12 21s-8-5.2-8-11a4.5 4.5 0 0 1 8-2.8A4.5 4.5 0 0 1 20 10c0 5.8-8 11-8 11z"/></svg>
        <h4>Free high-skilled<br>assessment and treatment</h4>
        <p>Students who qualify receive a full check-up, cleaning, x-rays and fillings on site.</p>
      </div>
      <div class="offer">
        <svg viewBox="0 0 24 24"><path fill="#fff" d="M4 4h16a2 2 0 0 1 2 2v9a2 2 0 0 1-2 2H10l-5 4v-4H4a2 2 0 0 1-2-2V6a2 2 0 0 1 2-2z"/></svg>
        <h4>One-on-one<br>oral health education</h4>
        <p>Each child gets simple brushing tips and advice to keep teeth healthy.</p>
      </div>
      <div class="offer">
        <svg viewBox="0 0 24 24"><circle cx="12" cy="9" r="6" fill="#fff"/><path fill="#fff" d="M8 14l-2 8 6-3 6 3-2-8z"/></svg>
        <h4>Win various<br>prizes drawing</h4>
        <p>Students enter a draw to win prizes for their visit to the clinic.</p>
      </div>
      <div class="offer">
        <svg viewBox="0 0 24 24"><rect x="2" y="2" width="20" height="20" rx="2" fill="none" stroke="#fff" stroke-width="2"/><path d="M6 12l4 4 8-8" fill="none" stroke="#fff" stroke-width="2.5"/></svg>
        <h4>Referral to your<br>regular dentist</h4>
        <p>We provide a referral for any further treatment they may require.</p>
      </div>
    </div>
  </div>
  <div class="about">
    <p>CWDG operates within accepted best practice models and as such complies with the Code of Conduct set by the <strong>Regional Dental Practice Board</strong>.</p>
    <p>Our mobile clinic features state of the art dental equipment, including digital x-ray and wheelchair access for every student.</p>
    <p>Thank you for considering CWDG. My team and I look forward to providing this free service to your school and, most importantly, bringing the dentist to you.</p>
  </div>
</section>

<section class="page cover">
  <div class="cover-top"></div>
  <div class="brand">
    <p class="name">Coastline Wandering Dental Group</p>
  </div>
  <div class="staff-photo" role="img" aria-label="Photo of two dental staff at work in the mobile clinic, tinted aqua"></div>
  <div class="focus">
    <p class="pre">Our focus is on</p>
    <p class="main">Education<br>&amp; Prevention</p>
  </div>
  <div class="quote">
    <blockquote>"1 in 5 children between the ages of 4-8 years of age will suffer from tooth decay or dental caries as a result of poor dental hygiene."</blockquote>
    <cite>The Southern Paediatric Health Council</cite>
    <p class="note">This leads to possible dental destruction to their adult teeth. This, in conjunction with diet, lifestyle and social welfare can be contributing to the increase of child absenteeism.</p>
  </div>
  <div class="cover-foot"></div>
</section>

</body>
</html>
```